Need an ebook cover for a memoir about growing up in NYC in the 90s and getting in lots of trouble.

Velvet Curb Chronicles is the true story of an over-privileged hoodlum
growing up in Manhattan in the 90s during the golden era of hip-hop. The book follows the troubled youth all the way from hanging off the back of subway cars at fourteen, through a romance with a mafia princess doomed for disaster, to a law school class where the unreformed miscreant sits politely with his hand raised. The cover should feature a white teenager, perhaps in a puffy Ridge Loom jacket, in NYC -- or whatever you feel; I am open. I've attached a sample of the memoir for your reference. I've also attached a sample of what I think the title should look like: Velvet Curb Chronicles; Corwin Halde; A Memoir.

The name of the author is Corwin Halde. It is not Milo Frick.

```html
<!DOCTYPE html>
<html lang="en">
<head>
<meta charset="UTF-8">
<title>Velvet Curb Chronicles — Corwin Halde</title>
<link rel="stylesheet" href="https://fonts.googleapis.com/css2?family=Lato:ital,wght@0,400;0,700;0,900;1,400&display=swap">
<style>
  :root {
    --frame-top: #ffd600;
    --frame-mid: #8a8a1f;
    --frame-bottom: #0b3147;
    --panel-top: #e5f3f8;
    --panel-bottom: #d3e9f3;
    --navy: #023047;
    --ink: #0a0a0a;
    --author: #0c3a52;
    --body: #222a30;
    --quote: #6a6f73;
    --gold: #c9a426;
    --brush: #ffd400;
  }
  * { margin: 0; padding: 0; box-sizing: border-box; }
  html, body { width: 846px; height: 1200px; overflow: hidden; background: #ffffff; }
  .cover {
    position: relative;
    width: 846px;
    height: 1200px;
    background: linear-gradient(to bottom, var(--frame-top) 0%, var(--frame-top) 12%, var(--frame-mid) 50%, var(--frame-bottom) 96%);
    font-family: "Lato", sans-serif;
    overflow: hidden;
  }
  .panel {
    position: absolute;
    left: 29px; top: 27px;
    width: 788px; height: 1146px;
    background: linear-gradient(to bottom, var(--panel-top), var(--panel-bottom));
  }
  .bestseller-band {
    position: absolute;
    left: 29px; top: 27px;
    width: 788px; height: 76px;
  }
  .bestseller-text {
    position: absolute;
    left: 92px; top: 51px;
    font-size: 33px;
    line-height: 1;
    font-weight: 900;
    color: #ffffff;
    letter-spacing: -0.3px;
    white-space: nowrap;
  }
  .title {
    position: absolute;
    left: 0; right: 0; top: 131px;
    text-align: center;
    font-size: 73px;
    line-height: 87px;
    font-weight: 700;
    color: var(--ink);
    letter-spacing: -0.5px;
  }
  .title span { display: block; }
  .portrait {
    position: absolute;
    left: 225px; top: 425px;
    width: 400px; height: 402px;
  }
  .author {
    position: absolute;
    left: 0; right: 0; top: 856px;
    text-align: center;
    font-size: 43px;
    line-height: 1;
    font-weight: 700;
    color: var(--author);
    letter-spacing: -0.3px;
  }
  .synopsis {
    position: absolute;
    left: 90px; right: 90px; top: 926px;
    text-align: center;
    font-size: 17px;
    line-height: 28px;
    font-weight: 700;
    color: var(--body);
  }
  .excerpt {
    position: absolute;
    left: 140px; right: 140px; top: 1001px;
    text-align: center;
    font-size: 16.5px;
    line-height: 29px;
    font-style: italic;
    color: var(--quote);
  }
  .genre {
    position: absolute;
    left: 0; right: 0; top: 1095px;
    text-align: center;
    font-size: 27px;
    line-height: 1;
    font-weight: 700;
    color: var(--gold);
  }
</style>
</head>
<body>
<div class="cover">
  <div class="panel"></div>

  <svg class="bestseller-band" viewBox="0 0 788 76" aria-hidden="true">
    <polygon points="0,0 788,0 754,76 0,76" fill="var(--navy)"/>
  </svg>
  <div class="bestseller-text">THE #1 METRO LEDGER BESTSELLER</div>

  <h1 class="title"><span>VELVET</span><span>CURB</span><span>CHRONICLES</span></h1>

  <svg class="portrait" viewBox="0 0 400 402">
    <defs>
      <linearGradient id="photoTone" x1="0" y1="0" x2="1" y2="1">
        <stop offset="0" stop-color="#2f433f"/>
        <stop offset="0.45" stop-color="#6b4a35"/>
        <stop offset="0.75" stop-color="#b38868"/>
        <stop offset="1" stop-color="#d4ad93"/>
      </linearGradient>
    </defs>
    <polygon points="190,2 330,70 366,200 346,300 215,395 60,350 10,230 40,70"
             fill="var(--brush)" transform="rotate(-6 200 200)"/>
    <polygon role="img" aria-label="Photo of a teenager with long hair covering their face with one hand"
             points="199,6 369,98 369,302 199,396 26,302 26,103" fill="url(#photoTone)"/>
  </svg>

  <div class="author">By Corwin Halde</div>

  <p class="synopsis">Velvet Curb Chronicles is the true story of an over-privileged hoodlum growing up in Manhattan in the 90s during the golden era of hip-hop.</p>

  <p class="excerpt">“I’m sixteen years old and I don’t give a fuck about anything except pussy and smoking pot. Sixteen is a great time to be alive, especially in Manhattan.”</p>

  <div class="genre">A MEMOIR</div>
</div>
</body>
</html>
```